Massage Therapy and Energy Healing Practice

I am a massage therapist, Reiki energy healer, I sell herbs and oils, and also a health lifestyle coach. I need a design that is strong because I'm not a spa. I do therapeutic work, but I want a touch of the energy and spiritual healing I do as well to be included in the design. I like blue, green, or purple colors. I live in the Blue Ridge Mountains of VA and even though my practice is in the city I like my love for nature and the earth to show through. I would like a single image logo so I can use the image many places. I need a strong brand that will let others know that I combine massage therapy in a therapeutic way while keeping my touches of energy healing, nurturing, herb crafting, and mother earth loving ways.
Updates

Just some things about me:I like to hike. I live on a farm. I own horses, cows, sheep and dogs. I love nature and the energy in produces. I'm very spiritual. I don't know how these things might help or if they do, but I know that my personality might help inspire what I will find good in a design. Added Sunday, December 13, 2015

Target Market(s)

People in pain. People who need spiritual council. Need herbal medicine advice. Holistic healthcare.

Industry/Entity Type

Massage

Contact Information for Business Card

Kneadwell Studio
Lorna T. Whitcombe C.M.T, R.M.T
40519 Hollin Creek Court, Tallowdale, VA
540-718-2437

Colors
3176b5
85abd2
876aae
9bcb3c

Requirements
Must have
• Strong Branding that promotes my massage therapy practice first
Nice to have
• Something to evoke my herbal medicine, my energy healing, my spiritual side

```html
<!DOCTYPE html>
<html lang="en">
<head>
<meta charset="utf-8">
<title>Kneadwell Studio – Business Card</title>
<link rel="stylesheet" href="https://fonts.googleapis.com/css2?family=Archivo+Black&family=Jost:wght@400;700&display=swap">
<style>
  :root {
    --green-deep: #16b062;
    --green-mid: #25c46f;
    --green-glow: #38dc89;
    --green-pale: #6ee3a0;
    --green-soft: #55d692;
    --brand-pink: #ef8fb8;
    --mark-teal: #2ac4c9;
    --ink-white: #ffffff;
  }
  html, body {
    margin: 0;
    padding: 0;
    width: 1200px;
    height: 649px;
    overflow: hidden;
  }
  .card {
    position: relative;
    width: 1200px;
    height: 649px;
    overflow: hidden;
    background: radial-gradient(ellipse 620px 360px at 560px 400px, var(--green-glow), var(--green-mid) 60%, var(--green-deep));
  }
  .card__waves {
    position: absolute;
    inset: 0;
  }
  .brand {
    position: absolute;
    left: 0;
    right: 0;
    top: 375px;
    text-align: center;
  }
  .brand__name {
    margin: 0;
    font-family: "Archivo Black", "Arial Black", sans-serif;
    font-size: 56px;
    line-height: 1;
    color: var(--brand-pink);
    letter-spacing: 0.3px;
  }
  .contact {
    position: absolute;
    left: 22px;
    top: 521px;
    font-family: "Jost", "Futura", sans-serif;
    color: var(--ink-white);
    line-height: 36px;
  }
  .contact__name {
    margin: 0;
    font-size: 24px;
    font-weight: 700;
    letter-spacing: 0.3px;
  }
  .contact__line {
    margin: 0;
    font-size: 25px;
    font-weight: 400;
    letter-spacing: 0.2px;
  }
</style>
</head>
<body>
  <main class="card">
    <svg class="card__waves" width="1200" height="649" viewBox="0 0 1200 649" aria-hidden="true">
      <path d="M0 0 H640 C420 40 200 150 0 400 Z" fill="var(--green-pale)" opacity="0.85"/>
      <path d="M1200 649 H560 C860 570 1080 420 1200 230 Z" fill="var(--green-soft)" opacity="0.9"/>
      <path d="M1200 649 H820 C1000 590 1130 500 1200 400 Z" fill="var(--green-pale)" opacity="0.45"/>
      <circle class="brand__mark" cx="600" cy="215" r="140" fill="var(--mark-teal)" opacity="0.75"/>
    </svg>

    <div class="brand">
      <h1 class="brand__name">Kneadwell Studio</h1>
    </div>

    <div class="contact">
      <p class="contact__name">Lorna T. Whitcombe C.M.T, R.M.T</p>
      <p class="contact__line">40519 Hollin Creek Court, Tallowdale, VA</p>
      <p class="contact__line">540-718-2437</p>
    </div>
  </main>
</body>
</html>
```